Kirevoli Tea & Dairy Farm Website

Design a mainly visual informational website incorporating examples uploaded of a tea and dairy farm in Africa. I can provide more pictures.

I do take suggestions willing.

Industry/Entity Type

Farm

Font styles to use
Serif

Colors
acd037

```html
<!DOCTYPE html>
<html lang="en">
<head>
<meta charset="utf-8">
<title>Kirevoli Tea &amp; Dairy Farm</title>
<link href="https://fonts.googleapis.com/css2?family=Ubuntu:wght@400;500&family=Open+Sans:wght@400;600&display=swap" rel="stylesheet">
<style>
:root{
  --green:#5f9f14;
  --green-light:#86c51f;
  --green-dark:#4f8c0e;
  --orange:#eeb208;
  --orange-deep:#e9a800;
  --text-grey:#8a8a8a;
  --text-dark:#333;
  --footer:#3b2a08;
  --white:#fff;
}
*{margin:0;padding:0;box-sizing:border-box}
html,body{width:979px;height:1200px;overflow:hidden;background:var(--white)}
body{font-family:"Open Sans",sans-serif;color:var(--text-grey)}
.page{position:relative;width:979px;height:1200px;overflow:hidden}
.abs{position:absolute}

.brand{left:86px;top:22px;color:var(--green);font-family:"Ubuntu",sans-serif;font-weight:400;line-height:1}
.brand .name{font-size:36px;display:block}
.brand .tag{font-size:13px;display:block;margin-top:6px}

.nav{left:0;top:96px;width:979px;height:50px;background:linear-gradient(var(--green-light),var(--green-dark));border-top:1px solid #9bd23a}
.nav ul{list-style:none;display:flex;position:absolute;left:87px;top:0;height:50px}
.nav li{font-family:"Ubuntu",sans-serif;font-weight:500;font-size:14.5px;color:var(--white);line-height:50px;padding:0 19px;border-right:1px solid rgba(0,0,0,.18);box-shadow:1px 0 0 rgba(255,255,255,.15)}
.nav li:first-child{padding-left:19px}
.nav li:last-child{border-right:none;box-shadow:none}

.hero-band{left:0;top:146px;width:979px;height:344px;background:linear-gradient(var(--green-light),#5a9a12);border-bottom:1px solid #3f7a08}
.hero-photo{left:75px;top:146px;width:830px;height:342px;background:linear-gradient(180deg,#8e9a88 0%,#6f8f46 25%,#8dbb2c 55%,#9fcb2d 80%,#7ea524 100%)}
.hero-banner{left:75px;top:284px;width:352px;height:114px}
.hero-text{left:102px;top:298px;color:var(--white);font-family:"Ubuntu",sans-serif}
.hero-text h1{font-weight:400;font-size:31px;line-height:1.1}
.hero-text .sub{font-size:15.5px;margin-top:4px}
.hero-text .small{font-size:9.5px;margin-top:7px}
.dots{left:460px;top:465px;display:flex;gap:4px}
.dots span{width:12px;height:12px;border-radius:50%;background:var(--white)}
.dots span.on{background:#111}

.features{left:0;top:490px;width:979px;height:222px;background:linear-gradient(#fff 70%,#f3f3f3)}
.feature{position:absolute;top:14px}
.feature .pic{height:113px}
.feature h2{font-family:"Ubuntu",sans-serif;font-weight:400;font-size:18.5px;color:var(--orange);margin-top:8px;margin-left:-6px}
.feature p{font-size:9.5px;line-height:16.5px;margin-top:4px;margin-left:-6px;width:262px}

.welcome{left:73px;top:748px;width:530px}
.welcome h2{font-family:"Ubuntu",sans-serif;font-weight:400;font-size:24px;color:var(--green)}
.welcome p{font-size:10.4px;line-height:18.3px;margin-top:5px;padding-left:2px}

.provide{position:absolute;top:912px;width:280px}
.provide .icon{position:absolute;left:0;top:0;width:72px;height:76px;border-radius:10px;background:var(--green-light)}
.provide h3{position:absolute;left:88px;top:0;font-family:"Ubuntu",sans-serif;font-weight:400;font-size:17px;color:var(--green-light)}
.provide p{position:absolute;left:90px;top:24px;width:190px;font-size:10.4px;line-height:19.5px}
.provide p .lead{color:#555}
.provide .more{position:absolute;left:90px;top:85px;font-size:10.8px;color:#666;font-weight:600}

.projects{left:650px;top:748px;width:270px}
.projects h2{font-family:"Ubuntu",sans-serif;font-weight:400;font-size:21px;color:#a98a1c}
.project{position:absolute;left:3px;width:265px}
.project .thumb{position:absolute;left:0;top:0;width:98px;height:67px;border:1px solid #ddd;box-shadow:0 1px 3px rgba(0,0,0,.2);padding:4px;background:#fff}
.project .thumb div{width:100%;height:100%}
.project h3{position:absolute;left:109px;top:2px;font-weight:400;font-size:12.5px;color:#333}
.project p{position:absolute;left:109px;top:21px;width:150px;font-size:9.6px;line-height:16.6px;color:#999}

.footer{left:0;top:1088px;width:979px;height:112px;background:var(--footer);border-top:2px solid #2c1f04}
.footer .links{position:absolute;left:78px;top:29px;font-family:"Ubuntu",sans-serif;font-size:12.5px;color:var(--white)}
.footer .links span.sep{margin:0 5px}
.footer .copy{position:absolute;left:78px;top:56px;font-size:9.5px;color:#cbbf9f}
.social{position:absolute;left:808px;top:28px;display:flex;gap:3px}
.social span{width:23px;height:23px;border-radius:50%;background:var(--white)}
</style>
</head>
<body>
<div class="page">

  <div class="abs brand">
    <span class="name">Kirevoli</span>
    <span class="tag">Tea &amp; Dairy Farm</span>
  </div>

  <nav class="abs nav">
    <ul>
      <li>Home</li><li>About Us</li><li>Our Farms</li><li>Services</li><li>Products</li><li>Opportunities</li><li>Projects</li><li>Contact Us</li>
    </ul>
  </nav>

  <div class="abs hero-band"></div>
  <div class="abs hero-photo" role="img" aria-label="Rolling green tea plantation hills beneath forested mountains"></div>
  <svg class="abs hero-banner" viewBox="0 0 352 114" aria-hidden="true">
    <defs><linearGradient id="bannerFill" x1="0" y1="0" x2="0" y2="1"><stop offset="0" stop-color="#f4bc10"/><stop offset="1" stop-color="#e9a600"/></linearGradient></defs>
    <polygon points="0,0 310,0 352,57 310,114 0,114" fill="url(#bannerFill)" opacity=".95"/>
  </svg>
  <div class="abs hero-text">
    <h1>Tea &amp; Dairy Farm</h1>
    <div class="sub">Donec scelerisque leo ac risus</div>
    <div class="small">Ut nisi erat fermentum vel congue id euismod in elit</div>
  </div>
  <div class="abs dots"><span class="on"></span><span></span><span></span><span></span></div>

  <section class="abs features">
    <div class="feature" style="left:78px;width:266px">
      <div class="pic" role="img" aria-label="Rows of tea bushes on a plantation" style="background:linear-gradient(160deg,#6fae2a,#3f8a1c 60%,#5a9c24)"></div>
      <h2>Animal Feeding Solutions</h2>
      <p>Class aptent taciti sociosqu ad litora torquent per conubia nostra per inceptos hymenaeos</p>
    </div>
    <div class="feature" style="left:361px;width:270px">
      <div class="pic" role="img" aria-label="Dairy cows lined up in a milking parlour" style="background:linear-gradient(180deg,#8a8f95,#cfd0d0 45%,#8c8a86)"></div>
      <h2>Dairy &amp; Farming</h2>
      <p>Class aptent taciti sociosqu ad litora torquent per conubia nostra per inceptos hymenaeos</p>
    </div>
    <div class="feature" style="left:646px;width:271px">
      <div class="pic" role="img" aria-label="Farmhouse kitchen interior with wooden cabinets" style="background:linear-gradient(135deg,#8a7561,#5e4330 55%,#c9c0b4)"></div>
      <h2>Services Provide</h2>
      <p>Class aptent taciti sociosqu ad litora torquent per conubia nostra per inceptos hymenaeos</p>
    </div>
  </section>

  <section class="abs welcome">
    <h2>Welcome to Our Website Mainpage</h2>
    <p>Sed metus augue convallis et vehicula ut pulvinar eu ante Integer orci tellus tristique vitae consequat nec porta vel lectus Nulla sit amet diam Duis non nunc Aliquam necerat at purus cursus interdum Vestibulum ligula augue bibendum accumsan vestibulum ut commodo a mi</p>
    <p>Morbi ornare gravida elit Integer congue augue et malesuada iaculis ipsum Etiam est nunc venenatis in tristique eu imperdiet ac nisl Cum sociis natoque penatibus et magnis dis parturient montes</p>
  </section>

  <div class="provide" style="left:77px">
    <div class="icon" role="img" aria-label="Green cow head with wheat sprig icon"></div>
    <h3>What We Provides</h3>
    <p><span class="lead">Ligula augue bibendum</span><br>accumsan vestibulum ut commodo a mi Morbi ornare gravida</p>
    <div class="more">Learn More</div>
  </div>
  <div class="provide" style="left:359px">
    <div class="icon" role="img" aria-label="Green leaves icon"></div>
    <h3 style="left:73px">What We Provides</h3>
    <p style="left:75px"><span class="lead">Ligula augue bibendum</span><br>accumsan vestibulum ut commodo a mi Morbi ornare gravida</p>
    <div class="more" style="left:75px">Learn More</div>
  </div>

  <section class="abs projects">
    <h2>Our Projects</h2>
    <div class="project" style="top:41px">
      <div class="thumb"><div role="img" aria-label="Brown cow grazing in a field" style="background:linear-gradient(135deg,#a45a2a,#8a8a3a 60%,#6fa03a)"></div></div>
      <h3>Aliquam nec erat</h3>
      <p>Class aptent taciti sociosqu ad litora torquent per conubia nostra per inceptos hym</p>
    </div>
    <div class="project" style="top:128px">
      <div class="thumb"><div role="img" aria-label="Seedling trays on greenhouse shelves" style="background:linear-gradient(180deg,#6f8a6a,#5fa73a 50%,#dfe6df)"></div></div>
      <h3>Etiam est nunc</h3>
      <p>Class aptent taciti sociosqu ad litora torquent per conubia nostra per inceptos hym</p>
    </div>
    <div class="project" style="top:215px">
      <div class="thumb"><div role="img" aria-label="Red dirt path beside tea rows" style="background:linear-gradient(160deg,#6e9a3a,#9a5a3a 50%,#4f8a2a)"></div></div>
      <h3>Donec scelerisque</h3>
      <p>Class aptent taciti sociosqu ad litora torquent per conubia nostra per inceptos hym</p>
    </div>
  </section>

  <footer class="abs footer">
    <div class="links">Home<span class="sep">|</span>About Us<span class="sep">|</span>Our Farms<span class="sep">|</span>Services<span class="sep">|</span>Products<span class="sep">|</span>Opportunities<span class="sep">|</span>Projects<span class="sep">|</span>Contact Us</div>
    <div class="copy">Copyright © 2014 Company Name.&nbsp; All right reseverd</div>
    <div class="social" aria-label="Social links"><span></span><span></span><span></span><span></span></div>
  </footer>

</div>
</body>
</html>
```